Commercial Business Card - stand out, clean, simple, unique.

commercial real estate group located in Texas. Called 4 Ridges Real Estate. We want a unique yet clean and professional card. On one side I would like the 4R to be by itself or to look as unique or tasteful as possible. We have the logo in white, black, and color in case a black background or something similar looks best on one side. We need a space for our name, email, cell. website. And possibly room for a phrase or city.

Contact Information for Business Card

Name, Title, Email, Phone Number, website

```html
<!DOCTYPE html>
<html lang="en">
<head>
<meta charset="utf-8">
<title>4 Ridges Real Estate – Business Card</title>
<link href="https://fonts.googleapis.com/css2?family=Cinzel:wght@700&family=Lato:wght@400&display=swap" rel="stylesheet">
<style>
  :root {
    --backdrop: #1e1e1f;
    --card: #ffffff;
    --navy: #1c2b5e;
    --orange: #e0793a;
    --ink: #111111;
    --rule: #2a2a2a;
  }
  * { box-sizing: border-box; margin: 0; padding: 0; }
  html, body { width: 1200px; height: 1200px; overflow: hidden; }
  body { background: var(--backdrop); position: relative; font-family: "Lato", sans-serif; }

  .card {
    position: absolute;
    left: 240px;
    width: 720px;
    height: 410px;
    background: var(--card);
    border-radius: 30px;
    box-shadow: 0 10px 28px rgba(0,0,0,0.45);
  }
  .card--front { top: 144px; }
  .card--back { top: 598px; }

  /* Front */
  .brand {
    position: absolute;
    top: 146px;
    left: 0; right: 0;
    display: flex;
    justify-content: center;
    align-items: center;
    gap: 24px;
  }
  .brand__mark {
    width: 92px;
    height: 92px;
    background: var(--navy);
  }
  .brand__rule { width: 1.5px; height: 116px; background: var(--rule); }
  .brand__name { line-height: 1; }
  .brand__name-main {
    display: block;
    font-family: "Cinzel", serif;
    font-weight: 700;
    font-size: 50px;
    color: var(--navy);
  }
  .brand__name-sub {
    display: block;
    font-family: "Lato", sans-serif;
    font-weight: 400;
    font-size: 21px;
    letter-spacing: 9.6px;
    color: var(--orange);
    margin-top: 8px;
  }
  .front__web {
    position: absolute;
    top: 355px; left: 0; right: 0;
    text-align: center;
    font-size: 16px;
    letter-spacing: 2.2px;
    color: var(--navy);
  }

  /* Back */
  .person {
    position: absolute;
    top: 182px;
    right: 408px;
    text-align: right;
  }
  .person__name {
    font-family: "Cinzel", serif;
    font-weight: 700;
    font-size: 30px;
    color: var(--navy);
    line-height: 1;
  }
  .person__title { font-size: 17px; color: var(--ink); margin-top: 8px; }
  .back__rule {
    position: absolute;
    left: 335px; top: 148px;
    width: 1.5px; height: 124px;
    background: var(--rule);
  }
  .contacts {
    position: absolute;
    left: 366px; top: 160px;
    list-style: none;
  }
  .contacts li {
    display: flex; align-items: center; gap: 12px;
    font-size: 17px; color: var(--ink);
    height: 28px;
  }
  .contacts svg { width: 15px; height: 15px; fill: var(--orange); flex: none; }
  .address {
    position: absolute;
    top: 346px; left: 0; right: 0;
    display: flex; justify-content: center; align-items: center; gap: 12px;
    font-size: 17px; color: var(--ink);
  }
  .address__mark {
    width: 32px;
    height: 32px;
    background: var(--navy);
    flex: none;
  }
</style>
</head>
<body>
  <section class="card card--front" aria-label="Card front">
    <div class="brand">
      <span class="brand__mark" role="img" aria-label="4 Ridges Real Estate mark"></span>
      <span class="brand__rule"></span>
      <span class="brand__name">
        <span class="brand__name-main">4 RIDGES</span>
        <span class="brand__name-sub">REAL ESTATE</span>
      </span>
    </div>
    <p class="front__web">www.4ridgesrealestate.com</p>
  </section>

  <section class="card card--back" aria-label="Card back">
    <div class="person">
      <p class="person__name">DANIEL HART</p>
      <p class="person__title">Founder &amp; CEO</p>
    </div>
    <span class="back__rule"></span>
    <ul class="contacts">
      <li>
        <svg viewBox="0 0 24 24" aria-hidden="true"><path d="M6.6 10.8a15.1 15.1 0 0 0 6.6 6.6l2.2-2.2a1 1 0 0 1 1-.25 11.4 11.4 0 0 0 3.6.6 1 1 0 0 1 1 1V20a1 1 0 0 1-1 1A17 17 0 0 1 3 4a1 1 0 0 1 1-1h3.5a1 1 0 0 1 1 1c0 1.25.2 2.45.6 3.6a1 1 0 0 1-.25 1z"/></svg>
        512 555 0148
      </li>
      <li>
        <svg viewBox="0 0 24 24" aria-hidden="true"><path d="M2 5h20v2.2l-10 6.3L2 7.2z"/><path d="M2 9.6l10 6.3 10-6.3V19H2z"/></svg>
        info@4ridgesrealestate.com
      </li>
      <li>
        <svg viewBox="0 0 24 24" aria-hidden="true"><path d="M12 2a10 10 0 1 0 0 20 10 10 0 0 0 0-20zm6.9 6h-3a15.6 15.6 0 0 0-1.3-3.9A8 8 0 0 1 18.9 8zM12 4c.8 1.2 1.5 2.5 1.9 4h-3.8c.4-1.5 1.1-2.8 1.9-4zM4.3 14a8.2 8.2 0 0 1 0-4h3.4a16 16 0 0 0 0 4zm.8 2h3a15.6 15.6 0 0 0 1.3 3.9A8 8 0 0 1 5.1 16zm3-8h-3a8 8 0 0 1 4.3-3.9A15.6 15.6 0 0 0 8.1 8zM12 20c-.8-1.2-1.5-2.5-1.9-4h3.8c-.4 1.5-1.1 2.8-1.9 4zm2.3-6H9.7a14 14 0 0 1 0-4h4.6a14 14 0 0 1 0 4zm.3 5.9a15.6 15.6 0 0 0 1.3-3.9h3a8 8 0 0 1-4.3 3.9zm1.7-5.9a16 16 0 0 0 0-4h3.4a8.2 8.2 0 0 1 0 4z"/></svg>
        www.4ridgesrealestate.com
      </li>
    </ul>
    <p class="address">
      <span class="address__mark" role="img" aria-label="4 Ridges Real Estate mark"></span>
      48 Ridgeline Road, Suite B, Austin, TX 78701
    </p>
  </section>
</body>
</html>
```